Corvanta LLC, providing clean, low emission fuel for the transport and maritime industry

Corvanta LLC is a Texas based company dedicated to the development of Small Scale LNG projects with the objective of supplying clean, low emission fuel to the transport and maritime industry.

The design should be simple and sophisticated. We want a design that includes our company logo and uses our company logo colors. The site should include 7 pages (Home, About, What is LNG, Projects, Announcements and Contact Us). The site should ultimately be editable and capable of being imported into WIX. The design should communicate an environmentally conscious company who provide "Simple, Practical, and Cost Effective Solutions". Our competitions website looks like this www.brenmarfuel.com.

Target Market(s)

LNG, maritime

Industry/Entity Type

Oil And Gas

Coding

Coded - Design and coding required

Number of Pages Required

5+ page

Requirements
Must have
• Equal or better than our competitors website www.brenmarfuel.com
Company Logo.
The tagline "Simple, Practical, and Cost Effective Solutions"
Nice to have
• The page content will be very similar to our competitors website www.brenmarfuel.com
Should not have
• No red or black colours.

```html
<!DOCTYPE html>
<html lang="en">
<head>
<meta charset="utf-8">
<title>Corvanta LLC — Simple Practical and Cost Effective Solutions</title>
<link href="https://fonts.googleapis.com/css2?family=Michroma&family=Open+Sans:wght@400;600;700&family=Poppins:wght@400;500;600&display=swap" rel="stylesheet">
<style>
:root{
  --navy:#0b2f7e;
  --navy-deep:#0a2766;
  --green:#2f8a2f;
  --ink:#1f2a3a;
  --text:#6b6b6b;
  --card:#ebebeb;
  --soft:#f7f7f7;
  --band:#e8e8e8;
  --field:#e6e6e6;
  --white:#ffffff;
}
*{margin:0;padding:0;box-sizing:border-box}
html,body{width:1200px;height:3381px;overflow:hidden;background:var(--white)}
body{position:relative;font-family:"Open Sans",sans-serif;color:var(--text)}
.abs{position:absolute}

/* header */
.site-header{left:0;top:0;width:1200px;height:84px;background:var(--navy)}
.brand{left:0;top:0;width:341px;height:84px;background:var(--white);display:flex;align-items:center;justify-content:center;gap:8px}
.brand-dot{width:22px;height:22px;border-radius:50%;background:var(--green)}
.brand-name{font-family:"Open Sans",sans-serif;font-weight:700;font-size:15px;color:var(--navy);letter-spacing:.5px}
.nav a{position:absolute;top:29px;font-family:"Open Sans",sans-serif;font-weight:600;font-size:15px;color:var(--white);text-decoration:none;white-space:nowrap}
.nav a.active{color:#5fae3a}
.nav-underline{left:485px;top:60px;width:50px;height:3px;background:var(--green)}

/* hero */
.hero{left:0;top:84px;width:1200px;height:557px;background:linear-gradient(180deg,#0d1730 0%,#1c2a44 45%,#3a3328 72%,#10182a 100%)}
.hero-title{left:0;top:250px;width:1200px;text-align:center;font-family:"Michroma",sans-serif;font-size:40px;line-height:50px;color:var(--white);letter-spacing:1px}
.hero-sub{left:0;top:389px;width:1200px;text-align:center;font-family:"Open Sans",sans-serif;font-size:14px;line-height:26px;color:var(--white)}
.hero-chevron{left:567px;top:517px}

/* section titles */
.section-title{left:0;width:1200px;text-align:center;font-family:"Michroma",sans-serif;font-size:33px;color:var(--ink)}
.section-title span{color:var(--navy)}
.rule{height:3px;background:var(--green)}

/* projects */
.project-card{top:819px;width:300px;height:418px;background:var(--card)}
.project-photo{width:300px;height:213px}
.project-card h3{position:absolute;left:24px;top:226px;font-family:"Michroma",sans-serif;font-weight:400;font-size:16px;color:var(--ink)}
.project-card p{position:absolute;left:24px;top:257px;width:262px;font-size:13px;line-height:26px;color:var(--text)}

/* LNG */
.lng-band{left:0;top:1333px;width:598px;height:499px;background:var(--soft)}
.lng-photo{left:598px;top:1333px;width:602px;height:499px;background:linear-gradient(160deg,#0f2a6e 0%,#2e3f6a 35%,#7d7a2e 65%,#1a2350 100%)}
.lng-title{left:117px;top:1420px;font-family:"Michroma",sans-serif;font-size:33px;color:var(--ink)}
.lng-title span{color:var(--navy)}
.lng-text{left:114px;top:1490px;width:423px;font-size:13px;line-height:25.7px;text-align:justify;color:var(--text)}

/* clients */
.clients-band{left:0;top:1832px;width:1200px;height:328px;background:var(--band)}
.client{top:2002px;height:63px;background:var(--white);display:flex;align-items:center;justify-content:center;gap:6px;font-family:"Open Sans",sans-serif;font-weight:600;font-size:12px;color:#3a3a3a}
.client i{width:10px;height:10px;background:#9a9a9a;display:block}

/* contact */
.map{left:112px;top:2334px;width:976px;height:440px;background:linear-gradient(135deg,#c8c7b8 0%,#d6d3c0 40%,#b9c3c6 75%,#7ea3c7 100%)}
.map-toggle{left:122px;top:2358px;width:156px;height:38px;background:var(--white);display:flex;align-items:center;justify-content:center;gap:14px;font-family:"Poppins",sans-serif;font-weight:500;font-size:15px;color:#222;box-shadow:0 1px 3px rgba(0,0,0,.25)}
.form-heading,.info-heading{font-family:"Poppins",sans-serif;font-weight:500;font-size:16px;color:#222}
.field-label{left:142px;font-family:"Poppins",sans-serif;font-size:13px;color:#666}
.field{left:142px;width:324px;height:40px;background:var(--field);font-family:"Poppins",sans-serif;font-size:13px;color:#a9a9a9;padding:10px 16px}
.field.message{height:91px}
.submit{left:343px;top:3249px;width:122px;height:40px;background:var(--navy);color:var(--white);font-family:"Poppins",sans-serif;font-weight:600;font-size:15px;display:flex;align-items:center;justify-content:center}
.info-line{left:675px;font-family:"Poppins",sans-serif;font-size:15px;color:#555;line-height:26px}
.inquiry{left:659px;top:3087px;font-family:"Poppins",sans-serif;font-size:15px;line-height:26px;color:#555}
.quote{left:661px;top:3194px;font-family:"Poppins",sans-serif;font-weight:600;font-size:16px;color:#222}

/* footer */
.footer-rule{left:0;top:3325px;width:1200px;height:1px;background:#cfcfcf}
.footer-text{left:134px;top:3334px;font-family:"Poppins",sans-serif;font-size:12.5px;color:#444}
.social{top:3331px;width:32px;height:31px;background:var(--navy)}
</style>
</head>
<body>

<header class="abs site-header">
  <div class="abs brand"><span class="brand-dot"></span><span class="brand-name">Corvanta LLC</span></div>
  <nav class="nav">
    <a class="active" style="left:490px">Home</a>
    <a style="left:567px">About</a>
    <a style="left:646px">What is LNG</a>
    <a style="left:768px">Projects</a>
    <a style="left:860px">Announcements</a>
    <a style="left:1011px">Contact Us</a>
  </nav>
  <div class="abs nav-underline"></div>
</header>

<section class="abs hero" role="img" aria-label="Offshore oil rig and port lit up at night, reflected in the water"></section>
<h1 class="abs hero-title">SIMPLE PRACTICAL AND COST<br>EFFECTIVE SOLUTIONS</h1>
<p class="abs hero-sub">Lorem ipsum dolor sit amet, consectetur adipiscing elit, sed do eiusmod tempor incididunt ut labore<br>et dolore magna aliqua</p>
<svg class="abs hero-chevron" width="66" height="40" viewBox="0 0 66 40"><polyline points="2,3 33,36 64,3" fill="none" stroke="#fff" stroke-width="3"/></svg>

<h2 class="abs section-title" style="top:730px">OUR <span>PROJECTS</span></h2>
<div class="abs rule" style="left:545px;top:782px;width:109px"></div>

<article class="abs project-card" style="left:125px">
  <div class="project-photo" role="img" aria-label="Silver fuel tanker truck on the road" style="background:linear-gradient(180deg,#6f8fbf 0%,#b9c2cc 50%,#5a5f5a 100%)"></div>
  <h3>LOREM IPSUM</h3>
  <p>Lorem ipsum dolor sit amet, consect etur adipiscing elit, sed do eiusmod tempor incididunt ut labore et dolore magna aliqua. Ut enim ad minim veniam, quis nostrud</p>
</article>
<article class="abs project-card" style="left:450px">
  <div class="project-photo" role="img" aria-label="Industrial refinery lit at night beside the water" style="background:linear-gradient(180deg,#0e2a8a 0%,#1a3a9a 55%,#b06a2a 70%,#0a1f60 100%)"></div>
  <h3>LOREM IPSUM</h3>
  <p>Lorem ipsum dolor sit amet, consect etur adipiscing elit, sed do eiusmod tempor incididunt ut labore et dolore magna aliqua. Ut enim ad minim veniam, quis nostrud</p>
</article>
<article class="abs project-card" style="left:776px">
  <div class="project-photo" role="img" aria-label="Large mining excavator machine at dusk" style="background:linear-gradient(180deg,#55626f 0%,#6a5a4a 55%,#8a4a2a 75%,#2a2420 100%)"></div>
  <h3>LOREM IPSUM</h3>
  <p>Lorem ipsum dolor sit amet, consect etur adipiscing elit, sed do eiusmod tempor incididunt ut labore et dolore magna aliqua. Ut enim ad minim veniam, quis nostrud</p>
</article>

<div class="abs lng-band"></div>
<div class="abs lng-photo" role="img" aria-label="Offshore gas platform illuminated against a deep blue night sky"></div>
<h2 class="abs lng-title">WHAT <span>IS LNG</span></h2>
<div class="abs rule" style="left:118px;top:1471px;width:112px"></div>
<p class="abs lng-text">Lorem ipsum dolor sit amet, consectetur adipiscing elit, sed do eiusmod tempor incididunt ut labore et dolore magna aliqua. Utenim ad minim veniam, quis nostrud exercitation ullamco lab oris nisi ut aliquip ex ea commodo consequat. Duis aute irure dolor in reprehenderit in voluptate velit esse cillum dolore eu fugiat nulla pariatur. Excepteur sint occaecat cupidatat non proident, sunt in culpa qui officia deserunt mollit anim id est laborum Duis aute irure dolor in reprehenderit in voluptate velit esse cillum dolore eu fugiat nulla</p>

<div class="abs clients-band"></div>
<h2 class="abs section-title" style="top:1918px">OUR <span>CLIENTS</span></h2>
<div class="abs rule" style="left:545px;top:1970px;width:109px"></div>
<div class="abs client" style="left:146px;width:109px"><i></i>Norvell</div>
<div class="abs client" style="left:336px;width:109px"><i></i>Ardenloop</div>
<div class="abs client" style="left:528px;width:106px"><i></i>Verdalis</div>
<div class="abs client" style="left:714px;width:113px"><i></i>Kestrova</div>
<div class="abs client" style="left:909px;width:105px"><i></i>Bramwick</div>

<h2 class="abs section-title" style="top:2249px">OUR <span>CONTACT</span></h2>
<div class="abs rule" style="left:545px;top:2301px;width:109px"></div>
<div class="abs map" role="img" aria-label="Road map of the United States"></div>
<div class="abs map-toggle"><span>MAP</span><span>SATELLITE</span></div>

<h3 class="abs form-heading" style="left:143px;top:2813px">Contact Us</h3>
<label class="abs field-label" style="top:2855px">Enter Your Name</label>
<div class="abs field" style="top:2884px">Name</div>
<label class="abs field-label" style="top:2938px">Enter Your Email</label>
<div class="abs field" style="top:2967px">Email</div>
<label class="abs field-label" style="top:3021px">Enter Your Subject</label>
<div class="abs field" style="top:3050px">Subject</div>
<label class="abs field-label" style="top:3104px">Enter Your message</label>
<div class="abs field message" style="top:3133px">message</div>
<div class="abs submit">SUBMIT</div>

<h3 class="abs info-heading" style="left:659px;top:2815px">Address</h3>
<p class="abs info-line" style="top:2857px">123, Lorem ipsum dolor sit<br>amet, consectetur</p>
<p class="abs info-line" style="top:2920px">info@corvantafuel.com</p>
<p class="abs info-line" style="top:2953px">Tel: 123-456-7890</p>
<p class="abs info-line" style="top:2984px">Fax: 123-456-7890</p>
<h3 class="abs info-heading" style="left:659px;top:3044px">Inquiries</h3>
<p class="abs inquiry">For any inquiries, questions or commendations,<br>please call: 123-456-7890 or fill out the following form</p>
<p class="abs quote">Get a quote: 123-456-7890</p>

<div class="abs footer-rule"></div>
<p class="abs footer-text">© 2020 Corvanta Terms and Conditions | Disclaimer | Privacy Policy</p>
<div class="abs social" style="left:996px"></div>
<div class="abs social" style="left:1040px"></div>

</body>
</html>
```